I WAS JUST GIVING A SIZE THAT THE LABEL NEEDS TO BE ON OUR PACKAGING BAGS, IT IS 4X6. PLEASE MAKE SURE THAT DESIGN WILL FIT ON THAT SIZE.

We are looking to have you design the packaging for our coffee that will be sold online. The basics that we want on all the different varieties is our company name "Dunbarry's Gourmet Coffee & tagline " Gourmet Coffee for the Everyday Coffee Lover" and logo which is attached. If you ffind a different logo and want to change the colors in the logo, we are open to any suggestions. Our thoughts are travel the world with your coffee, that why we went with compass star. We are looking to use black bags for all as well. We would like a different picture background that is relatable to the type of coffee, if possible. The colors need to pop on the black bag. We need designs for the following flavors of coffee...

Brazilian Dark Roast
Columbian Supremo
100% Columbian Dark Roast
French Vanilla
Meadow Rhapsody
Kona Blend
Jamaican Blue Mountain Blend
Sumatra
Hazelnut
Irish Cream
Hawaiian Macadamia Nut Blend
Amaretto

All these flavors will be sold in 5# and 2# packages

```html
<!DOCTYPE html>
<html lang="en">
<head>
<meta charset="utf-8">
<title>Dunbarry's Gourmet Coffee – Brasilian Dark Roast Label</title>
<link rel="stylesheet" href="https://fonts.googleapis.com/css2?family=Cormorant+SC:wght@500&family=Oswald:wght@400&display=swap">
<style>
  :root {
    --bag-black: #000000;
    --band-green: #009444;
    --map-grey: #1f1f1f;
    --map-grey-soft: #151515;
    --compass-gold: #c9a23a;
    --text-white: #ffffff;
    --fine-grey: #4a4a4a;
    --web-grey: #5a5a5a;
  }
  html, body {
    margin: 0;
    padding: 0;
    overflow: hidden;
    background: var(--bag-black);
  }
  .label {
    position: relative;
    width: 801px;
    height: 1200px;
    background: var(--bag-black);
    overflow: hidden;
    font-family: "Cormorant SC", "Times New Roman", serif;
    font-weight: 500;
    color: var(--text-white);
  }
  .world-map {
    position: absolute;
    left: 50px;
    top: 252px;
    width: 693px;
    height: 384px;
    border-radius: 45% 40% 35% 45% / 40% 45% 40% 50%;
    background: radial-gradient(ellipse at 50% 45%, var(--map-grey) 0%, var(--map-grey-soft) 60%, var(--bag-black) 100%);
  }
  .brand-mark {
    position: absolute;
    left: 321px;
    top: 277px;
    width: 152px;
    height: 152px;
  }
  .brand-name {
    position: absolute;
    left: 0;
    width: 100%;
    text-align: center;
    margin: 0;
    line-height: 1;
  }
  .brand-name--main {
    top: 452px;
    font-size: 74px;
    letter-spacing: 1px;
  }
  .brand-name--sub {
    font-size: 40px;
    letter-spacing: 3px;
  }
  .brand-name--gourmet { top: 541px; }
  .brand-name--coffee { top: 587px; }
  .rule {
    position: absolute;
    left: 0;
    width: 100%;
    background: var(--band-green);
  }
  .rule--top-thin { top: 663px; height: 6px; }
  .variety-band {
    position: absolute;
    left: 0;
    top: 675px;
    width: 100%;
    height: 61px;
    background: var(--band-green);
    display: flex;
    align-items: center;
    justify-content: center;
    font-size: 34px;
    letter-spacing: 1px;
  }
  .rule--bottom-thin { top: 742px; height: 6px; }
  .tagline {
    position: absolute;
    top: 815px;
    left: 0;
    width: 100%;
    text-align: center;
    margin: 0;
    font-size: 36px;
    line-height: 36px;
    letter-spacing: 0.5px;
  }
  .credits {
    position: absolute;
    top: 1002px;
    left: 0;
    width: 100%;
    text-align: center;
    margin: 0;
    font-size: 18px;
    line-height: 21px;
    color: var(--fine-grey);
  }
  .rule--weight-top { top: 1054px; height: 4px; }
  .net-weight {
    position: absolute;
    top: 1068px;
    left: 0;
    width: 100%;
    text-align: center;
    margin: 0;
    font-family: "Oswald", "Arial Narrow", sans-serif;
    font-weight: 400;
    font-size: 20px;
    line-height: 24px;
  }
  .rule--weight-bottom { top: 1108px; height: 4px; }
  .website {
    position: absolute;
    top: 1130px;
    left: 0;
    width: 100%;
    text-align: center;
    margin: 0;
    font-family: "Cormorant SC", "Times New Roman", serif;
    font-size: 23px;
    text-transform: lowercase;
    color: var(--web-grey);
  }
</style>
</head>
<body>
  <main class="label">
    <div class="world-map" role="img" aria-label="Faint dark grey world map silhouette behind the brand name"></div>

    <svg class="brand-mark" viewBox="0 0 152 152" aria-hidden="true">
      <circle cx="76" cy="76" r="62" fill="none" stroke="var(--compass-gold)" stroke-width="8"/>
    </svg>

    <h1 class="brand-name brand-name--main">Dunbarry's</h1>
    <p class="brand-name brand-name--sub brand-name--gourmet">GOURMET</p>
    <p class="brand-name brand-name--sub brand-name--coffee">COFFEE</p>

    <div class="rule rule--top-thin"></div>
    <div class="variety-band">Brasilian Dark Roast</div>
    <div class="rule rule--bottom-thin"></div>

    <p class="tagline">Gourmet Coffee for the<br>Everyday Coffee Lover</p>

    <p class="credits">Roasted and Packed by Hearthstone Roasters<br>Distributed by Dunbarry's Gourmet Coffee</p>

    <div class="rule rule--weight-top"></div>
    <p class="net-weight">netto weight 5 oz</p>
    <div class="rule rule--weight-bottom"></div>

    <p class="website">www.dunbarrysgourmetcoffee.com</p>
  </main>
</body>
</html>
```